Kalo Motors logo

Please create a business card for us. Use the bottom left red logo and colours only.

Tobias Wendell
Director
Phone: +263 772 806 413
Email: toby@kalomotors.co.zw

Address: 18 Fenton road, Belvedere, Harare

```html
<!DOCTYPE html>
<html lang="en">
<head>
<meta charset="UTF-8">
<title>Kalo Motors – Business Card</title>
<link rel="stylesheet" href="https://fonts.googleapis.com/css2?family=Oswald:wght@500;600&family=Roboto:wght@400;500&display=swap">
<style>
  :root {
    --brand-red: #ec2227;
    --brand-grey: #8a8a8a;
    --ink: #333333;
    --paper: #ffffff;
    --backdrop: #e9e9e9;
  }
  * { margin: 0; padding: 0; box-sizing: border-box; }
  html, body { width: 1200px; height: 900px; overflow: hidden; }
  body {
    background: var(--backdrop);
    position: relative;
    font-family: "Roboto", sans-serif;
  }
  .card {
    position: absolute;
    width: 540px;
    height: 310px;
    border-radius: 22px;
    overflow: hidden;
    box-shadow: 0 6px 18px rgba(0,0,0,0.18);
  }
  .card-front {
    left: 60px; top: 110px;
    background: var(--brand-red);
    display: flex; align-items: center; justify-content: center;
  }
  .card-back {
    left: 600px; top: 470px;
    background: var(--paper);
  }
  .brand {
    display: flex; align-items: center; gap: 14px;
  }
  .brand-dot {
    width: 22px; height: 22px; border-radius: 50%;
  }
  .brand-name {
    font-family: "Oswald", sans-serif;
    font-weight: 600;
    font-size: 44px;
    letter-spacing: 1px;
    text-transform: uppercase;
    line-height: 1;
  }
  .card-front .brand-dot { background: var(--paper); }
  .card-front .brand-name { color: var(--paper); }

  .card-back .brand {
    position: absolute; left: 36px; top: 108px;
  }
  .card-back .brand-dot { background: var(--brand-grey); width: 16px; height: 16px; }
  .card-back .brand-name { color: var(--brand-red); font-size: 30px; }

  .divider {
    position: absolute; left: 262px; top: 42px;
    width: 2px; height: 150px; background: var(--brand-red);
  }
  .contact {
    position: absolute; left: 280px; top: 40px;
  }
  .person-name {
    font-family: "Oswald", sans-serif;
    font-weight: 600;
    font-size: 24px;
    color: var(--brand-red);
    text-transform: uppercase;
    line-height: 1.1;
  }
  .person-role {
    font-family: "Oswald", sans-serif;
    font-weight: 500;
    font-size: 14px;
    color: var(--ink);
    text-transform: uppercase;
    margin-bottom: 12px;
  }
  .contact-list { list-style: none; }
  .contact-item {
    display: flex; align-items: center; gap: 8px;
    font-size: 14px; color: var(--ink);
    margin-bottom: 6px;
  }
  .contact-icon { width: 13px; height: 13px; fill: var(--brand-red); flex: none; }
  .footer-bands {
    position: absolute; left: 0; bottom: 0; width: 540px; height: 80px;
  }
</style>
</head>
<body>

  <section class="card card-front">
    <div class="brand">
      <span class="brand-dot"></span>
      <span class="brand-name">Kalo Motors</span>
    </div>
  </section>

  <section class="card card-back">
    <div class="brand">
      <span class="brand-dot"></span>
      <span class="brand-name">Kalo Motors</span>
    </div>

    <div class="divider"></div>

    <div class="contact">
      <h1 class="person-name">Tobias Wendell</h1>
      <p class="person-role">Director</p>
      <ul class="contact-list">
        <li class="contact-item">
          <svg class="contact-icon" viewBox="0 0 24 24"><path d="M6.6 10.8a15.1 15.1 0 0 0 6.6 6.6l2.2-2.2a1 1 0 0 1 1-.25 11.4 11.4 0 0 0 3.6.57 1 1 0 0 1 1 1V20a1 1 0 0 1-1 1A17 17 0 0 1 3 4a1 1 0 0 1 1-1h3.5a1 1 0 0 1 1 1c0 1.25.2 2.45.57 3.57a1 1 0 0 1-.25 1z"/></svg>
          +263 772 806 413
        </li>
        <li class="contact-item">
          <svg class="contact-icon" viewBox="0 0 24 24"><path d="M2 5h20v14H2z M2 5l10 8 10-8" /></svg>
          toby@kalomotors.co.zw
        </li>
        <li class="contact-item">
          <svg class="contact-icon" viewBox="0 0 24 24"><circle cx="12" cy="12" r="10"/></svg>
          www.kalodrive.co.zw
        </li>
        <li class="contact-item">
          <svg class="contact-icon" viewBox="0 0 24 24"><path d="M12 3 2 12h3v9h5v-6h4v6h5v-9h3z"/></svg>
          18 Fenton road, Belvedere, Harare
        </li>
      </ul>
    </div>

    <svg class="footer-bands" viewBox="0 0 540 80" preserveAspectRatio="none">
      <polygon points="0,58 400,58 380,80 0,80" fill="var(--brand-red)"/>
      <polygon points="420,0 540,0 540,80 360,80" fill="var(--brand-grey)"/>
      <polygon points="410,10 540,10 540,58 380,58" fill="var(--brand-grey)"/>
    </svg>
  </section>

</body>
</html>
```